Need a graphic design for front page of tech blog

Hi,

So I'm looking to start a project of redesigning the front homepage for all of my tech sites. I already have a developer that will code the change, so what I need from someone here is to give me a graphic design, which I can then give to my developers to code.

Currently, I have the plain old boring default list of WordPress posts as the front page, which needs to be replaced with something a little more like a magazine or newspaper style. You can see my four sites here:

https://www.quill-gadget-notes.com/
https://servicebenchnerd.com/
https://theatticbitworks.com/
https://www.hoppingtolark.com/

I've attached some screenshots of mobile sites that I like in terms of look and style. Some desktop sites that I like are here (I like some parts more than others, I've attached screenshots of the sections I like):

https://www.ploddernook.com/
https://www.gizmonest.com/
https://www.pinewirebulletin.com/
https://www.takeholdwith.com/
https://www.dayspool.com/

Basically, I don't need all that text after each post. Seems like most sites now just have an image, a title, the author and date info and possibly the category.

Right now I'm only showing 10 posts and one has to scroll through lots of text to see them all. The sidebar is good, but I think we can get rid of that for the front page and instead have different sections like Latest Tips, and then some section headers based on the categories.

Anyway, I'm looking for someone who can come up with multiple designs, so that I have some choice.

I'm looking to get this done over the next few weeks. Also, please include in your price the cost of any revisions and how many revisions can be done.

Thanks

Tarun

```html
<!DOCTYPE html>
<html lang="en">
<head>
<meta charset="utf-8">
<title>Quill Gadget Notes — Home</title>
<link href="https://fonts.googleapis.com/css2?family=Lato:wght@400;700;900&display=swap" rel="stylesheet">
<style>
:root{
  --orange:#f0541e;
  --orange-deep:#e04a12;
  --ink:#1e1e1e;
  --text:#222;
  --muted:#555;
  --panel:#f1f1f1;
  --line:#d6d6d6;
  --footer:#1c1c1c;
  --footer-text:#9a9a9a;
  --white:#fff;
}
*{box-sizing:border-box;margin:0;padding:0}
html,body{width:1200px;height:3056px;overflow:hidden}
body{font-family:'Lato',sans-serif;color:var(--text);background:var(--white);position:relative}
.abs{position:absolute}

/* header */
.site-header{position:absolute;left:0;top:0;width:1200px;height:96px;background:var(--white)}
.brand{position:absolute;left:140px;top:30px;display:flex;align-items:center;gap:8px;font-weight:900;font-size:28px;color:var(--ink);letter-spacing:.5px}
.brand .dot{width:18px;height:18px;border-radius:50%;background:var(--orange)}
.main-nav{position:absolute;left:510px;top:38px;display:flex;gap:26px;font-size:14px;font-weight:700;color:var(--ink)}
.search{position:absolute;left:845px;top:28px;width:213px;height:42px;border:2px solid #bbb;border-radius:21px}
.search svg{position:absolute;left:14px;top:11px}

/* hero */
.hero{position:absolute;left:0;top:96px;width:1200px;height:424px;background:linear-gradient(120deg,#1b2024 0%,#2c3338 45%,#4a3d32 75%,#222 100%)}
.hero-arrow{position:absolute;top:172px;width:50px;height:50px;border-radius:50%;background:rgba(160,160,160,.55)}
.hero-arrow.prev{left:60px}.hero-arrow.next{left:1060px}
.hero-arrow svg{position:absolute;left:16px;top:15px}
.hero-tag{position:absolute;left:165px;top:112px;background:var(--orange);color:var(--white);font-size:15px;font-weight:700;padding:7px 17px}
.hero-title{position:absolute;left:165px;top:152px;color:var(--white);font-size:29px;font-weight:900;line-height:32px;width:520px;text-transform:uppercase}
.hero-meta{position:absolute;left:165px;top:228px;color:#eee;font-size:16px;line-height:32px;text-transform:uppercase}

/* latest posts */
.latest-posts{position:absolute;left:0;top:520px;width:1200px;height:1285px;background:var(--panel)}
.section-title{position:absolute;left:0;width:1200px;text-align:center;font-size:30px;font-weight:900;color:var(--ink)}
.post-card{position:absolute;width:428px;height:198px;background:var(--white);border:1px solid var(--line);box-shadow:0 1px 3px rgba(0,0,0,.08)}
.post-card .thumb{position:absolute;left:20px;top:20px;width:200px;height:156px}
.post-card .body{position:absolute;left:234px;top:24px;width:180px}
.cat{color:var(--orange);font-size:13px;font-weight:700;text-transform:uppercase}
.post-card h3{font-size:16px;font-weight:700;line-height:19px;margin-top:10px;color:var(--ink)}
.post-card .meta{font-size:13px;line-height:20px;color:var(--muted);margin-top:10px}

/* latest tips */
.latest-tips .section-title{color:var(--orange)}
.tip-card{position:absolute;top:1893px;width:282px;height:310px;background:var(--white);border:1px solid var(--line);box-shadow:0 1px 3px rgba(0,0,0,.1)}
.tip-card .thumb{width:100%;height:160px}
.tip-card .body{padding:14px 20px}
.tip-card .cat{text-transform:none;font-size:13px}
.tip-card h3{font-size:16px;font-weight:700;line-height:20px;margin-top:8px;color:var(--ink)}
.tip-card .meta{font-size:13px;line-height:20px;color:var(--muted);margin-top:8px}

/* newsletter */
.newsletter{position:absolute;left:0;top:2272px;width:1200px;height:393px}
.newsletter svg.band{position:absolute;left:0;top:0}
.newsletter h2{position:absolute;left:0;top:100px;width:1200px;text-align:center;color:var(--white);font-size:33px;font-weight:900}
.newsletter p{position:absolute;left:280px;top:152px;width:640px;text-align:center;color:rgba(255,255,255,.8);font-size:16px;line-height:20px}
.news-form{position:absolute;left:262px;top:216px;width:678px;height:62px;background:var(--white);border-radius:31px}
.news-form span{position:absolute;left:36px;top:20px;color:#888;font-size:18px}
.news-form .btn{position:absolute;left:510px;top:8px;width:156px;height:46px;border-radius:23px;background:#111;color:var(--white);font-size:20px;font-weight:700;text-align:center;line-height:46px}

/* footer */
.site-footer{position:absolute;left:0;top:2665px;width:1200px;height:391px;background:var(--footer);color:var(--footer-text)}
.f-brand{position:absolute;left:170px;top:76px;display:flex;align-items:center;gap:6px;color:#e6e6e6;font-size:21px;font-weight:900}
.f-brand .dot{width:12px;height:12px;border-radius:50%;background:#e6e6e6}
.f-about{position:absolute;left:172px;top:110px;width:200px;font-size:14px;line-height:23px}
.f-head{position:absolute;top:76px;color:var(--white);font-size:18px;font-weight:700}
.f-links{position:absolute;left:458px;top:100px;list-style:none;font-size:14px;line-height:23px}
.f-sign p{position:absolute;left:652px;top:104px;width:260px;font-size:14px;line-height:23px}
.f-input{position:absolute;left:650px;top:162px;width:256px;height:36px;border-radius:18px;background:var(--white);color:#555;font-size:13px;padding:10px 18px}
.f-btn{position:absolute;left:652px;top:209px;width:108px;height:34px;border-radius:17px;background:var(--orange);color:var(--white);font-size:12px;font-weight:900;text-align:center;line-height:34px}
.f-social{position:absolute;left:966px;top:112px;list-style:none;font-size:14px}
.f-social li{display:flex;align-items:center;gap:10px;height:32px;color:#cfcfcf}
.f-social .ic{width:22px;height:22px;border-radius:50%;border:1.5px solid #cfcfcf}
.copyright{position:absolute;left:0;top:315px;width:1200px;border-top:1px solid #333;padding-top:21px;text-align:center;font-size:13px}
</style>
</head>
<body>

<header class="site-header">
  <div class="brand"><span class="dot"></span>QUILL GADGET NOTES</div>
  <nav class="main-nav"><span>DESKTOP OS</span><span>TIPS</span><span>SOFTWARE</span><span>OTHERS</span></nav>
  <div class="search"><svg width="16" height="16" viewBox="0 0 16 16"><circle cx="6.5" cy="6.5" r="5" fill="none" stroke="#999" stroke-width="2"/><line x1="10.5" y1="10.5" x2="15" y2="15" stroke="#999" stroke-width="2"/></svg></div>
</header>

<section class="hero" role="img" aria-label="Photo of a hooded person typing on a laptop showing code in a dark room">
  <div class="hero-arrow prev"><svg width="18" height="20" viewBox="0 0 18 20"><path d="M12 2 L4 10 L12 18" fill="none" stroke="#222" stroke-width="3"/></svg></div>
  <div class="hero-arrow next"><svg width="18" height="20" viewBox="0 0 18 20"><path d="M6 2 L14 10 L6 18" fill="none" stroke="#222" stroke-width="3"/></svg></div>
  <div class="hero-tag">COMPUTER TIPS</div>
  <h1 class="hero-title">How to Know If Your Password Has Leaked Online</h1>
  <div class="hero-meta">February 27th, 2019<br>By Colin Marsh File</div>
</section>

<section class="latest-posts">
  <h2 class="section-title" style="top:34px">LATEST POSTS</h2>
</section>

<article class="post-card" style="left:162px;top:626px">
  <div class="thumb" role="img" aria-label="Colourful cartoon show thumbnails" style="background:linear-gradient(90deg,#f3b42c,#e56a2a,#8cc63f)"></div>
  <div class="body"><div class="cat">Web Site Tips</div><h3>How To Use StreamBox's Parental Control Feature</h3><div class="meta">March 1st, 2019<br>by Dean Ashworth</div></div>
</article>
<article class="post-card" style="left:607px;top:626px">
  <div class="thumb" role="img" aria-label="Phone showing a pink lock screen keypad" style="background:linear-gradient(90deg,#7a2a8c,#e0559e,#3d7bd6)"></div>
  <div class="body"><div class="cat">Smartphones</div><h3>Can You Bypass the Droidware Lock Screen?</h3><div class="meta">March 1st, 2019<br>by Dean Ashworth</div></div>
</article>
<article class="post-card" style="left:162px;top:844px">
  <div class="thumb" role="img" aria-label="Illustration of a person working at a desk" style="background:linear-gradient(135deg,#cfe4f5,#6fa8dc,#e8e8f0)"></div>
  <div class="body"><div class="cat">Software Reviews</div><h3>Top 10 Collaboration Tools for Remote Teams</h3><div class="meta">March 1st, 2019<br>by Dean Ashworth</div></div>
</article>
<article class="post-card" style="left:607px;top:844px">
  <div class="thumb" role="img" aria-label="Phone screens showing a blue wallpaper and battery charts" style="background:linear-gradient(90deg,#f2f2f2,#2a5fd0,#e6e6e6)"></div>
  <div class="body"><div class="cat">Smartphones</div><h3>Droidware Pie (version 9) Review – The "Techie" Smartphone OS Gets</h3><div class="meta">March 1st, 2019<br>by Dean Ashworth</div></div>
</article>
<article class="post-card" style="left:162px;top:1060px">
  <div class="thumb" role="img" aria-label="Browser start page with a clock over a dark landscape" style="background:linear-gradient(160deg,#3b4a3e,#1e2622)"></div>
  <div class="body"><div class="cat">Searchco Software/Tips</div><h3>The Best Glimmer Extensions for Productivity</h3><div class="meta">March 1st, 2019<br>by Dean Ashworth</div></div>
</article>
<article class="post-card" style="left:607px;top:1060px">
  <div class="thumb" role="img" aria-label="Hand editing a printed manuscript with a red pen" style="background:linear-gradient(135deg,#ece9e4,#d9c8c8,#f3f1ee)"></div>
  <div class="body"><div class="cat">Software Reviews</div><h3>How to Be the Next Steinwell: Three Editing Tools for Writers</h3><div class="meta">March 1st, 2019<br>by Dean Ashworth</div></div>
</article>
<article class="post-card" style="left:162px;top:1277px">
  <div class="thumb" role="img" aria-label="Three smartphones in black, silver and purple" style="background:linear-gradient(90deg,#111,#9aa0a8,#c9c9cf,#a37aa8)"></div>
  <div class="body"><div class="cat">Smartphones</div><h3>Stellar Nova Note 9 Review</h3><div class="meta" style="margin-top:44px">February 20th, 2019<br>by Warren Holt</div></div>
</article>
<article class="post-card" style="left:607px;top:1277px">
  <div class="thumb" role="img" aria-label="Note reading new password on an orange background" style="background:linear-gradient(135deg,#e3924a,#f0a560,#f5efe6)"></div>
  <div class="body"><div class="cat">Software Reviews</div><h3>How To Set Up &amp; Use The VaultKeep Password Manager</h3><div class="meta">March 1st, 2019<br>by Dean Ashworth</div></div>
</article>
<article class="post-card" style="left:162px;top:1497px">
  <div class="thumb" role="img" aria-label="Close-up of an analogue electricity meter" style="background:linear-gradient(135deg,#8f9091,#c8c8c8,#5a5b5c)"></div>
  <div class="body"><div class="cat">Smart Home</div><h3>How to Monitor Your Home Electricity Usage</h3><div class="meta">March 1st, 2019<br>by Dean Ashworth</div></div>
</article>
<article class="post-card" style="left:607px;top:1497px">
  <div class="thumb" role="img" aria-label="Black printer next to a smart speaker" style="background:linear-gradient(180deg,#f5f5f5,#2a2a2a 70%,#1a1a1a)"></div>
  <div class="body"><div class="cat">Smart Home</div><h3>The State of Smart Home Printer Technology</h3><div class="meta">March 1st, 2019<br>by Dean Ashworth</div></div>
</article>

<section class="latest-tips">
  <h2 class="section-title" style="top:1835px">LATEST TIPS</h2>
  <article class="tip-card" style="left:162px">
    <div class="thumb" role="img" aria-label="Phone with envelopes flying from the screen" style="background:linear-gradient(135deg,#2c6fb8,#8fc0ea,#e8eef4)"></div>
    <div class="body"><div class="cat">Computer Tips</div><h3>Can Someone Know When I've Opened Their Email?</h3><div class="meta">February 12th, 2019<br>by Colin Marsh</div></div>
  </article>
  <article class="tip-card" style="left:462px">
    <div class="thumb" role="img" aria-label="Phone screen with messaging app icons" style="background:linear-gradient(135deg,#2a2a2a,#3aa85a,#1d6fb0)"></div>
    <div class="body"><div class="cat">Computer Tips</div><h3>Is Your Messaging App Really Secure?</h3><div class="meta">February 12th, 2019<br>by Colin Marsh</div></div>
  </article>
  <article class="tip-card" style="left:767px">
    <div class="thumb" role="img" aria-label="Grid of freelance service listings" style="background:linear-gradient(180deg,#e9e4f0,#f5f5f5,#6e6e6e)"></div>
    <div class="body"><div class="cat">Computer Tips</div><h3>How To Create Video Subtitles Quickly For Free</h3><div class="meta">February 12th, 2019<br>by Colin Marsh</div></div>
  </article>
</section>

<section class="newsletter">
  <svg class="band" width="1200" height="393" viewBox="0 0 1200 393">
    <rect x="0" y="0" width="1200" height="393" fill="#fff"/>
    <polygon points="0,96 600,0 1200,96 1200,393 0,393" fill="#3a3a3a"/>
    <polygon points="0,104 600,12 1200,104 1200,393 0,393" fill="url(#nl)" role="img" aria-label="Orange-tinted photo of people working together"/>
    <defs><linearGradient id="nl" x1="0" y1="0" x2="1" y2="1"><stop offset="0" stop-color="#f06a2a"/><stop offset=".5" stop-color="#e9541c"/><stop offset="1" stop-color="#d9480f"/></linearGradient></defs>
  </svg>
  <h2>SIGN UP OUR NEWSLETTERS</h2>
  <p>Aattis laoreet viverra sit amet quam Curabitur vel dolor ultrices ipsum dictum tristique Praesent vitae lacus Ut velit enim vestibulum non</p>
  <div class="news-form"><span>Your Email address</span><div class="btn">Subscribe</div></div>
</section>

<footer class="site-footer">
  <div class="f-brand"><span class="dot"></span>QUILL GADGET NOTES</div>
  <p class="f-about">Aattis laoreet viverra sit amet quam Curabitur vel dolor ultrices ipsum dictum tristique Praesent vitae lacus Ut velit enim</p>
  <div class="f-head" style="left:458px">QUICK LINKS</div>
  <ul class="f-links"><li>Home</li><li>About Us</li><li>Desktop OS</li><li>Tips</li><li>Software</li><li>Others</li></ul>
  <div class="f-sign">
    <div class="f-head" style="left:652px">SIGN UP TO RECEIVE EMAIL</div>
    <p>Excepteur sint occaecat cupidatat non proident, sunt in culpa qui</p>
    <div class="f-input">Enter Email</div>
    <div class="f-btn">SUBSCRIBE</div>
  </div>
  <div class="f-head" style="left:966px">SOCIAL</div>
  <ul class="f-social"><li><span class="ic"></span>Friendbook</li><li><span class="ic"></span>Chirper</li><li><span class="ic"></span>Circles+</li><li><span class="ic"></span>ClipTube</li></ul>
  <div class="copyright">Copyright © 2019 All right reserved</div>
</footer>

</body>
</html>
```